Continuing Professional Development Seminars
Power Point Template
• 11 juin 2011 15:52 rubenqol
thanks Velmoro
• 9 juin 2011 11:07 Velmoro
congrats your first project :)
• 9 juin 2011 02:48 tkvolaris
rubenqol - can you please upload a new draft that has the following slides:
1 - The title slide from draft#15 (I think this might be exactly the same in all subsequent drafts)
2 - The content slide from draft#15
3 - The content slide from draft#66
4 - The content slide from draft#68
5 - The last slide from draft#69
6 - The last slide from draft#15
I would like to see both of the end slides in the same draft.
Thanks.
• 7 juin 2011 08:20 tkvolaris
Thank you to all the designers who have submitted designs to date. The quality of the work is outstanding and is making the decision difficult.
I am still considering ALL the designs and will probably make a final decision soon. However, the designs that seem to stand out at the moment include (in no particular order) draft#50/draft#72, draft#15 (and the variations), draft#62 and draft#54.
• 6 juin 2011 06:31 tkvolaris
Draft#15 – can you please make the following changes:
1. Replace the last slide with a variant of the first slide. This new slide should be the same as the first slide, but with the following changes:
• The colours of the main background graphic should be reversed – so that becomes a red graphic with a blue stipe (instead of a blue graphic with a red stripe).
• Change the text - “Welcome to our Presentation” to “Thank you”.
• Change the white text (location and date) to the contact details you currently have on the last slide.
2. Can we try three small variations to the header on the content slides? Firstly, can you make the line under the presentation header about an inch smaller (so that it doesn’t go all the way to the logo). Secondly, can you please do a variant that reverses the logo and the header title (so that the logo is on the right and the presentation title is on the left). Thirdly, can you try a variant that doesn’t have the presentation header at all – only the logo? I would prefer having a look at all three slides to see how it looks. Thanks.
• 2 juin 2011 06:02 tkvolaris
Some of the recent designs have been very good. I particularly like the very bold graphical styles on the front pages whilst I prefer the more minimalist approach to the content slides.
I know that I said previously to try using our logo as a background watermark. However, on second thoughts I don’t think it really works. The watermarks are OK on the first slides, but on the content slides it is very distracting.
So far, my favourite designs are draft#15 and drafts#25-26. However, many of the designs have things I like or don’t like. Specifically,
• Draft#25 and Draft #26 – These designs are very effective. A bold front page and simple content pages. I think we would need to lose the watermarks on the content pages, but otherwise, these designs are on the right track.
• Draft#23 – I like the footer design of each content slide. Very simple and elegant.
• Draft#15 – perhaps my favourite design so far. Good bold first slide. The content slides are also good – maybe a little too busy as the moment?
• Draft#9 and Draft#10 – The first slides in these designs are very good. I like the strong bold designs. The content pages don’t really work – too much graphical background and not enough white space for content. One thing I like about these designs is the reverse colours of the background on the final slides.
Some of the other designs have similar good and bad points. However, I think I would be repeating myself if I discussed each one.
In summary, I like the first slides that are bold and emphasise our brand. The content slides should be simple, elegant and consistent.
• 31 mai 2011 19:56 tkvolaris
When I was looking through other projects on this website, there is one that I found that seems to be very effective. The project name is "Brisk Lanterns PowerPoint Template" and the design is draft#39.
I am not suggesting that I want a copy or a redraft of this design. It is just an example of something that I like.
• 31 mai 2011 19:47 tkvolaris
I like the designs that are creatively using the "swirls" on our logo. The first pages in draft#9 and draft#10 are interesting. I also didn't mind the first page in draft#11 (but note that it has been withdrawn?).
I think the logo needs to be more subtle on the content pages - maybe in the bottom right corner? Also maybe could use the logo as a watermark? Draft#4 uses a watermark, but being in the middle of the page, it might be a little distracting.

```html
<!DOCTYPE html>
<html lang="en">
<head>
<meta charset="utf-8">
<title>NOVIA Presentation Template</title>
<link rel="stylesheet" href="https://fonts.googleapis.com/css2?family=Open+Sans:wght@400;600;700&display=swap">
<style>
  :root {
    --board: #1e1e1e;
    --slide: #ffffff;
    --blue: #2f6fc0;
    --blue-soft: #8fa9d8;
    --red: #e03a3e;
    --red-soft: #f1a3a5;
    --ink: #1a1a1a;
    --body: #777777;
    --grid: #d6d6d6;
  }
  * { box-sizing: border-box; margin: 0; padding: 0; }
  html, body { width: 1200px; height: 907px; overflow: hidden; }
  body {
    background: var(--board);
    font-family: "Open Sans", Arial, sans-serif;
    position: relative;
  }
  .slide {
    position: absolute;
    width: 541px;
    height: 408px;
    background: var(--slide);
    overflow: hidden;
  }
  .slide--title { left: 44px; top: 30px; }
  .slide--list { left: 615px; top: 30px; }
  .slide--chart { left: 44px; top: 467px; }
  .slide--closing { left: 615px; top: 467px; }
  .decor { position: absolute; inset: 0; width: 100%; height: 100%; }
  .brand {
    position: absolute;
    font-weight: 700;
    color: var(--blue);
    letter-spacing: 1px;
  }
  .brand--large { left: 40px; top: 44px; font-size: 44px; }
  .brand--small { right: 26px; bottom: 22px; font-size: 22px; }
  .brand--center { left: 0; right: 0; top: 100px; text-align: center; font-size: 50px; }
  .cover-title {
    position: absolute; right: 36px; top: 315px; text-align: right;
  }
  .cover-title h1 { font-size: 25px; font-weight: 400; color: var(--blue); }
  .cover-title p { font-size: 18px; color: var(--red); margin-top: 2px; }
  .header { position: absolute; left: 28px; top: 28px; }
  .header h2 { font-size: 22px; font-weight: 700; color: var(--blue); letter-spacing: .3px; }
  .header h2 span { color: var(--red); }
  .header p { font-size: 12px; color: var(--ink); margin-top: 0; }
  .groups { position: absolute; list-style: none; width: 215px; }
  .groups li { position: relative; padding-left: 16px; margin-bottom: 16px; }
  .groups li::before {
    content: ""; position: absolute; left: 0; top: 4px;
    width: 8px; height: 8px; border-radius: 50%;
    border: 1.5px solid #999;
  }
  .groups h3 { font-size: 11px; font-weight: 700; color: var(--ink); }
  .groups p { font-size: 8.5px; line-height: 1.3; color: var(--body); }
  .groups--left { left: 30px; top: 128px; }
  .groups--right { left: 300px; top: 128px; }
  .groups--chart { left: 310px; top: 120px; }
  .groups--chart li { margin-bottom: 14px; }
  .chart { position: absolute; left: 20px; top: 102px; width: 270px; height: 240px; }
  .closing { position: absolute; left: 0; right: 0; top: 225px; text-align: center; }
  .closing h2 { font-size: 26px; font-weight: 700; color: var(--ink); }
  .closing p { font-size: 19px; font-weight: 700; color: var(--ink); }
</style>
</head>
<body>

<section class="slide slide--title">
  <svg class="decor" viewBox="0 0 541 408" aria-hidden="true">
    <path d="M-20 330 Q250 150 560 250" fill="none" stroke="var(--red-soft)" stroke-width="16"/>
    <path d="M-20 420 Q230 190 560 275" fill="none" stroke="var(--blue-soft)" stroke-width="34"/>
  </svg>
  <div class="brand brand--large">NOVIA</div>
  <div class="cover-title">
    <h1>TITLE OF PRESENTATION</h1>
    <p>Description</p>
  </div>
</section>

<section class="slide slide--list">
  <svg class="decor" viewBox="0 0 541 408" aria-hidden="true">
    <path d="M-20 400 Q260 230 560 330" fill="none" stroke="var(--red-soft)" stroke-width="10" opacity=".45"/>
    <path d="M-20 430 Q240 260 560 360" fill="none" stroke="var(--blue-soft)" stroke-width="22" opacity=".35"/>
  </svg>
  <header class="header">
    <h2>SAMPLES OF CONTENT <span>LIST</span></h2>
    <p>Description in this line</p>
  </header>
  <ul class="groups groups--left">
    <li><h3>Group 3</h3><p>Lorem ipsum dolor sit amet, consectetur adipiscing elit. Maecenas lobortis sollicitudin neque eget iaculis.</p></li>
    <li><h3>Group 4</h3><p>Lorem ipsum dolor sit amet, consectetur adipiscing elit. Maecenas lobortis sollicitudin neque eget iaculis.</p></li>
  </ul>
  <ul class="groups groups--right">
    <li><h3>Group 3</h3><p>Lorem ipsum dolor sit amet, consectetur adipiscing elit. Maecenas lobortis sollicitudin neque eget iaculis.</p></li>
    <li><h3>Group 4</h3><p>Lorem ipsum dolor sit amet, consectetur adipiscing elit. Maecenas lobortis sollicitudin neque eget iaculis.</p></li>
    <li><h3>Group 5</h3><p>Lorem ipsum dolor sit amet, consectetur adipiscing elit. Maecenas lobortis sollicitudin neque eget iaculis.</p></li>
    <li><h3>Group 6</h3><p>Lorem ipsum dolor sit amet, consectetur adipiscing elit. Maecenas lobortis sollicitudin neque eget iaculis.</p></li>
  </ul>
  <div class="brand brand--small">NOVIA</div>
</section>

<section class="slide slide--chart">
  <svg class="decor" viewBox="0 0 541 408" aria-hidden="true">
    <path d="M-20 400 Q260 230 560 330" fill="none" stroke="var(--red-soft)" stroke-width="10" opacity=".45"/>
    <path d="M-20 430 Q240 260 560 360" fill="none" stroke="var(--blue-soft)" stroke-width="22" opacity=".35"/>
  </svg>
  <header class="header">
    <h2>SAMPLES OF CONTENT <span>LIST</span></h2>
    <p>Description in this line</p>
  </header>
  <svg class="chart" viewBox="0 0 270 240" font-family="Open Sans, Arial, sans-serif" font-size="7" fill="#555">
    <g stroke="var(--grid)" stroke-width="1">
      <line x1="20" y1="10" x2="265" y2="10"/><line x1="20" y1="35" x2="265" y2="35"/>
      <line x1="20" y1="60" x2="265" y2="60"/><line x1="20" y1="85" x2="265" y2="85"/>
      <line x1="20" y1="110" x2="265" y2="110"/><line x1="20" y1="135" x2="265" y2="135"/>
      <line x1="20" y1="160" x2="265" y2="160"/><line x1="20" y1="185" x2="265" y2="185"/>
    </g>
    <line x1="20" y1="10" x2="20" y2="210" stroke="#999"/>
    <line x1="20" y1="210" x2="265" y2="210" stroke="#999"/>
    <g text-anchor="end">
      <text x="15" y="13">8</text><text x="15" y="38">7</text><text x="15" y="63">6</text>
      <text x="15" y="88">5</text><text x="15" y="113">4</text><text x="15" y="138">3</text>
      <text x="15" y="163">2</text><text x="15" y="188">1</text><text x="15" y="213">0</text>
    </g>
    <rect x="30" y="52" width="38" height="158" fill="var(--blue)"/>
    <rect x="91" y="137" width="38" height="73" fill="var(--red)"/>
    <rect x="152" y="180" width="38" height="30" fill="var(--blue)"/>
    <rect x="213" y="182" width="38" height="28" fill="var(--red)"/>
    <g text-anchor="middle">
      <text x="49" y="224">Group 1</text><text x="110" y="224">Group 2</text>
      <text x="171" y="224">Group 3</text><text x="232" y="224">Group 4</text>
    </g>
  </svg>
  <ul class="groups groups--chart">
    <li><h3>Group 3</h3><p>Lorem ipsum dolor sit amet, consectetur adipiscing elit. Maecenas lobortis sollicitudin neque eget iaculis.</p></li>
    <li><h3>Group 4</h3><p>Lorem ipsum dolor sit amet, consectetur adipiscing elit. Maecenas lobortis sollicitudin neque eget iaculis.</p></li>
    <li><h3>Group 5</h3><p>Lorem ipsum dolor sit amet, consectetur adipiscing elit. Maecenas lobortis sollicitudin neque eget iaculis.</p></li>
    <li><h3>Group 6</h3><p>Lorem ipsum dolor sit amet, consectetur adipiscing elit. Maecenas lobortis sollicitudin neque eget iaculis.</p></li>
  </ul>
  <div class="brand brand--small">NOVIA</div>
</section>

<section class="slide slide--closing">
  <svg class="decor" viewBox="0 0 541 408" aria-hidden="true">
    <path d="M-20 330 Q260 170 560 250" fill="none" stroke="var(--red-soft)" stroke-width="10" opacity=".35"/>
    <path d="M-20 380 Q240 200 560 290" fill="none" stroke="var(--blue-soft)" stroke-width="24" opacity=".25"/>
  </svg>
  <div class="brand brand--center">NOVIA</div>
  <div class="closing">
    <h2>THANK YOU FOR YOU ATTENTION</h2>
    <p>Author</p>
  </div>
</section>

</body>
</html>
```